Gift Voucher For Medical Cosmetic Clinic

I need a high end, beautiful gift voucher for my Cosmetic Medical Clinic that I will provide to customers in a beautifully designed envelope. I like the colours blue with different tones of blue, white and silver. I have attached my business card for further information.
The address is: 4/15 Kelbrook Lane, Tollbrook, Christchurch 8041.
Phone: 0800-547-391
Email: lorel@vumeko.co.nz
Website: www.vumeko.co.nz

```html
<!DOCTYPE html>
<html lang="en">
<head>
<meta charset="utf-8">
<title>Vumeko Gift Voucher</title>
<link href="https://fonts.googleapis.com/css2?family=Cormorant+Garamond:ital,wght@1,500&family=Marcellus&family=Open+Sans:wght@400;600;700&display=swap" rel="stylesheet">
<style>
  :root {
    --backdrop: #d3d3d3;
    --teal-deep: #1c4152;
    --teal-mid: #3f6a7b;
    --teal-light: #9fb8c2;
    --glow: #e9f0f2;
    --gold: #e0b34a;
    --gold-dark: #a8741c;
    --cream: #f3e6a6;
    --red: #e3141b;
    --white: #ffffff;
    --silver: #dfe4e6;
    --navy: #1b2a8c;
  }
  * { box-sizing: border-box; margin: 0; padding: 0; }
  html, body { width: 1200px; height: 800px; overflow: hidden; }
  body {
    background: var(--backdrop);
    font-family: "Open Sans", sans-serif;
    position: relative;
  }

  /* ---------- gift card ---------- */
  .gift-card {
    position: absolute;
    left: 330px; top: 36px;
    width: 540px; height: 310px;
    border-radius: 24px;
    overflow: hidden;
    background: radial-gradient(ellipse at 70% 40%, var(--teal-mid) 0%, var(--teal-deep) 75%);
    box-shadow: 0 10px 22px rgba(0,0,0,.25);
  }
  .gift-card__texture {
    position: absolute;
    left: 40px; top: 24px;
    width: 280px; height: 170px;
    background: linear-gradient(160deg, #0f2430 0%, #16323f 70%, rgba(22,50,63,0) 100%);
  }
  .gift-card__frame { position: absolute; left: 40px; top: 24px; }
  .gift-card__title {
    position: absolute;
    left: 92px; top: 46px;
    font-family: "Cormorant Garamond", serif;
    font-style: italic;
    font-weight: 500;
    color: var(--gold);
    line-height: .9;
  }
  .gift-card__title .word-gift { display: block; font-size: 40px; }
  .gift-card__title .word-card { display: block; font-size: 66px; padding-left: 40px; }

  .brand {
    position: absolute;
    right: 34px; top: 34px;
    font-family: "Marcellus", serif;
    font-size: 34px;
    letter-spacing: 3px;
    color: var(--cream);
  }
  .services {
    position: absolute;
    right: 34px; top: 92px;
    list-style: none;
    text-align: right;
    color: var(--white);
    font-size: 16px;
    line-height: 24px;
  }
  .services li::after {
    content: "";
    display: inline-block;
    width: 9px; height: 9px;
    margin-left: 8px;
    border-radius: 50%;
    background: var(--red);
    vertical-align: middle;
  }
  .tagline {
    position: absolute;
    left: 40px; top: 206px;
    color: var(--white);
    font-family: "Marcellus", serif;
    font-size: 17px;
    letter-spacing: 1.5px;
  }
  .contact-band {
    position: absolute;
    left: 0; bottom: 0;
    width: 100%; height: 58px;
    background: linear-gradient(180deg, var(--white), var(--silver));
    padding: 9px 40px;
    color: var(--navy);
    font-size: 12px;
    font-weight: 700;
    line-height: 20px;
  }

  /* ---------- envelopes ---------- */
  .envelope {
    position: absolute;
    top: 470px;
    width: 490px; height: 300px;
    overflow: hidden;
    background: radial-gradient(circle at 32% 50%, var(--glow) 0%, var(--teal-light) 18%, var(--teal-mid) 50%, var(--teal-deep) 100%);
    box-shadow: 4px 6px 14px rgba(0,0,0,.2);
  }
  .envelope--back { left: 90px; }
  .envelope--front { left: 620px; }
  .envelope__flap {
    position: absolute;
    left: 0; top: 0;
    width: 160px; height: 300px;
    border-radius: 0 24px 24px 0;
    background: radial-gradient(circle at 60% 40%, var(--glow) 0%, var(--teal-light) 30%, var(--teal-mid) 100%);
    box-shadow: 3px 0 8px rgba(0,0,0,.2);
  }
  .envelope__brand {
    position: absolute;
    right: 34px; top: 24px;
    font-family: "Marcellus", serif;
    font-size: 44px;
    letter-spacing: 4px;
    color: var(--silver);
  }
</style>
</head>
<body>

  <section class="gift-card" aria-label="Gift card front">
    <div class="gift-card__texture" role="img" aria-label="Dark brush-stroke texture behind the title"></div>
    <svg class="gift-card__frame" width="290" height="180" viewBox="0 0 290 180">
      <rect x="14" y="14" width="250" height="150" fill="none" stroke="var(--red)" stroke-width="6" transform="rotate(-4 139 89)"/>
      <rect x="34" y="22" width="220" height="134" fill="none" stroke="var(--white)" stroke-width="5" transform="rotate(5 144 89)"/>
    </svg>
    <h1 class="gift-card__title">
      <span class="word-gift">Gift</span>
      <span class="word-card">Card</span>
    </h1>

    <div class="brand">VUMEKO</div>

    <ul class="services">
      <li>Dermal Injectables</li>
      <li>Plasma Facials</li>
      <li>Microneedling</li>
      <li>Skin Boosters</li>
      <li>Excessive Sweating</li>
    </ul>

    <p class="tagline">VUMEKO-YOUR LOCAL COSMETIC CLINIC</p>

    <address class="contact-band">
      4/15 Kelbrook Lane, Tollbrook, Christchurch 8041.<br>
      P:0800-547-391 | E:lorel@vumeko.co.nz | W:www.vumeko.co.nz
    </address>
  </section>

  <section class="envelope envelope--back" aria-label="Envelope back">
    <div class="envelope__flap"></div>
  </section>

  <section class="envelope envelope--front" aria-label="Envelope front">
    <div class="envelope__brand">VUMEKO</div>
  </section>

</body>
</html>
```